Clear Plastic Card Design

I am looking to have a business card designed from my logo icon. I am looking to match the style of a different business card I have attached in the files.
Looking for a card that is plastic, with layers of transparency in the shape of my logo icon (also attached in the files) - not a circle like the other card. The winning design will incorporate the red icon logo on the front and back and include the charity's name, "Lanterns for the Weary" in the same or similar font, as well as an email and phone number. For now, use the email: email@lanternsfortheweary.org and the phone number 555-318-4072.
We like how the sample business card has transparency, partial and full opacity layers and a matching color scheme. Files will need to be in vector so that our business card printing company can work with it.
UPDATE:
We've some excellent designs in, thank you everyone! I got an early review from the owner, and he requested a minor redirect to find his perfect design. He wants the design to stand out by NOT being a rectangle. Try instead a circle, square, or best yet - something that falls in the outline of the logo icon, either fully or partially. Thank you, everyone!
Contact Information for Business Card
Lanterns for the Weary text should be incorporated as well as a phone and email.
Look and feel

```html
<!DOCTYPE html>
<html lang="en">
<head>
<meta charset="utf-8">
<title>Lanterns for the Weary – Business Card</title>
<link href="https://fonts.googleapis.com/css2?family=Poppins:wght@400;600;700&display=swap" rel="stylesheet">
<style>
  :root {
    --ink: #1a1a1a;
    --brand-red: #e0312b;
    --brand-crimson: #d81b4a;
    --edge-red: #e8413c;
    --line-orange: #f07a3a;
    --card-top: #fdf2ea;
    --card-bottom: #f6d3d3;
    --page: #ffffff;
  }
  html, body {
    margin: 0;
    padding: 0;
    width: 1200px;
    height: 400px;
    overflow: hidden;
    background: var(--page);
    font-family: "Poppins", sans-serif;
    color: var(--ink);
  }
  .stage {
    position: relative;
    width: 1200px;
    height: 400px;
  }
  .card-shapes {
    position: absolute;
    inset: 0;
  }
  .text {
    position: absolute;
    margin: 0;
    white-space: nowrap;
    line-height: 1;
  }
  .brand-lockup {
    font-size: 11px;
    line-height: 1.15;
    font-weight: 400;
    color: var(--ink);
  }
  .brand-lockup--small { font-size: 7.5px; }
  .charity-name {
    font-size: 21px;
    line-height: 1.08;
    font-weight: 400;
  }
  .charity-name .accent { color: var(--brand-red); }
  .mark-name {
    font-size: 19px;
    line-height: 1.15;
    font-weight: 600;
    color: #ffffff;
    text-align: center;
    width: 196px;
  }
  .person-name {
    font-size: 16px;
    font-weight: 700;
    color: var(--brand-crimson);
  }
  .person-role {
    font-size: 14.5px;
    font-weight: 400;
  }
  .contact-line {
    font-size: 10.5px;
    font-weight: 400;
  }
</style>
</head>
<body>
<main class="stage">
  <svg class="card-shapes" width="1200" height="400" viewBox="0 0 1200 400" aria-hidden="true">
    <defs>
      <linearGradient id="card-fill" x1="0" y1="0" x2="0" y2="1">
        <stop offset="0" stop-color="var(--card-top)"/>
        <stop offset="1" stop-color="var(--card-bottom)"/>
      </linearGradient>
      <filter id="card-shadow" x="-20%" y="-20%" width="140%" height="150%">
        <feDropShadow dx="6" dy="8" stdDeviation="6" flood-color="#000" flood-opacity="0.16"/>
      </filter>
    </defs>

    <!-- front card -->
    <g class="card card--front">
      <path class="card-half card-half--left" d="M324,70 L204,70 A135.5,135.5 0 0 0 204,341 L324,341 Z"
            fill="url(#card-fill)" stroke="var(--edge-red)" stroke-width="0.8" filter="url(#card-shadow)"/>
      <path class="card-half card-half--right" d="M362,70 L406,70 A135.5,135.5 0 0 1 406,341 L362,341 Z"
            fill="url(#card-fill)" stroke="var(--edge-red)" stroke-width="0.8" filter="url(#card-shadow)"/>
      <path class="layer-line" d="M362,85 L406,85 A120.5,120.5 0 0 1 406,326 L362,326" fill="none" stroke="var(--edge-red)" stroke-width="0.5"/>
      <path class="layer-line" d="M362,99 L406,99 A106.5,106.5 0 0 1 406,312 L362,312" fill="none" stroke="var(--line-orange)" stroke-width="0.5"/>
      <rect class="brand-square" x="192" y="124" width="28" height="28" fill="var(--brand-red)"/>
      <rect class="mark-block" x="296" y="110" width="196" height="196" fill="var(--brand-red)"/>
    </g>

    <!-- back card -->
    <g class="card card--back">
      <path class="card-half card-half--left" d="M917,70 L797,70 A135.5,135.5 0 0 0 797,341 L917,341 Z"
            fill="url(#card-fill)" stroke="var(--edge-red)" stroke-width="0.8" filter="url(#card-shadow)"/>
      <path class="card-half card-half--right" d="M955,70 L999,70 A135.5,135.5 0 0 1 999,341 L955,341 Z"
            fill="url(#card-fill)" stroke="var(--edge-red)" stroke-width="0.8" filter="url(#card-shadow)"/>
      <path class="layer-line" d="M955,85 L999,85 A120.5,120.5 0 0 1 999,326 L955,326" fill="none" stroke="var(--edge-red)" stroke-width="0.5"/>
      <path class="layer-line" d="M955,99 L999,99 A106.5,106.5 0 0 1 999,312 L955,312" fill="none" stroke="var(--line-orange)" stroke-width="0.5"/>
      <rect class="brand-square" x="737" y="114" width="22" height="22" fill="var(--brand-red)"/>
      <rect class="mark-block" x="889" y="110" width="196" height="196" fill="var(--brand-red)"/>

      <!-- phone icon -->
      <g class="icon icon--phone" transform="translate(709,256)">
        <circle r="6.5" fill="#fbe3e3" stroke="var(--edge-red)" stroke-width="0.6"/>
        <path d="M-2.6,-3.2 L-1.2,-3.4 L-0.4,-1.4 L-1.3,-0.7 Q-0.6,1 1,1.6 L1.6,0.7 L3.4,1.5 L3.2,2.8 Q-3.4,3 -2.6,-3.2 Z" fill="var(--brand-red)"/>
      </g>
      <!-- mail icon -->
      <g class="icon icon--mail" transform="translate(709,282)">
        <circle r="6.5" fill="#fbe3e3" stroke="var(--edge-red)" stroke-width="0.6"/>
        <rect x="-3.6" y="-2.5" width="7.2" height="5" fill="var(--brand-red)"/>
        <path d="M-3.6,-2.5 L0,0.6 L3.6,-2.5" fill="none" stroke="#fbe3e3" stroke-width="0.6"/>
      </g>
    </g>
  </svg>

  <!-- front card text -->
  <p class="text brand-lockup" style="left:109px; top:163px;">Lanterns for the<br>Weary</p>
  <h1 class="text charity-name" style="left:108px; top:221px;">Lanterns for the<br><span class="accent">Weary</span></h1>
  <p class="text mark-name" style="left:296px; top:186px;">Lanterns for<br>the Weary</p>

  <!-- back card text -->
  <p class="text brand-lockup brand-lockup--small" style="left:702px; top:138px;">Lanterns for the<br>Weary</p>
  <p class="text mark-name" style="left:889px; top:186px;">Lanterns for<br>the Weary</p>
  <h2 class="text person-name" style="left:702px; top:194px;">Dana Whitlock</h2>
  <p class="text person-role" style="left:702px; top:212px;">Marketing Director</p>
  <p class="text contact-line" style="left:727px; top:250px;">555-318-4072</p>
  <p class="text contact-line" style="left:727px; top:276px;">email@lanternsfortheweary.org</p>
</main>
</body>
</html>
```